Antigen Preservation Bureau

The company will provide a contract research services to stabilize various viruses, viral vectors, and vaccines. It may offer some licensing opportunities for stabilizing technologies. Main area of applications are pharmaceutical, therapeutic, and vaccination field. The company aspires to develop room temperature vaccines for global distribution beyond the current cold chain.

Target Market(s)

pharmaceutical, therapeutic and vaccination fields

Coding

Coded - Design and coding required

Number of Pages Required

4 page

Requirements
Must have
• Incorporate a APB logo, attached at the bottom, on the Web page

```html
<!DOCTYPE html>
<html lang="en">
<head>
<meta charset="utf-8">
<title>Antigen Preservation Bureau</title>
<link href="https://fonts.googleapis.com/css2?family=Poppins:wght@400;500;600;700&display=swap" rel="stylesheet">
<style>
:root{
  --teal:#2b8a7c;
  --orange:#e38a1f;
  --gold:#c8a04a;
  --ink:#1e2326;
  --body:#4d5458;
  --muted:#8a9094;
  --line:#e6e6e6;
  --bg:#ffffff;
}
*{box-sizing:border-box;margin:0;padding:0}
html,body{width:686px;height:1200px;overflow:hidden;background:var(--bg)}
body{font-family:"Poppins",sans-serif;color:var(--body);position:relative}
.abs{position:absolute}
/* header */
.site-header{left:0;top:0;width:686px;height:46px;border-bottom:1px solid var(--line)}
.brand{display:flex;align-items:center;gap:6px;font-size:9px;font-weight:600;color:var(--teal);line-height:1.1;text-transform:uppercase;width:110px}
.brand-dot{width:18px;height:18px;border-radius:50%;background:var(--teal);flex:none}
.site-header .brand{left:40px;top:10px}
.nav{right:40px;top:16px;display:flex;gap:22px;font-size:9px;color:var(--ink)}
.nav a{color:inherit;text-decoration:none}
.nav .active{color:var(--orange);border-bottom:2px solid var(--orange);padding-bottom:3px}
/* hero */
.hero-title{left:40px;top:78px;width:290px;font-size:17px;font-weight:700;line-height:1.35;color:var(--teal)}
.hero-text{left:40px;top:156px;width:260px;font-size:7px;line-height:1.6;color:var(--muted)}
.btn{display:inline-block;background:var(--orange);color:#fff;font-size:8px;font-weight:500;padding:7px 16px;border-radius:2px}
.hero .btn{left:40px;top:198px}
.art{background:linear-gradient(160deg,#eef3f2,#cfe2dd 55%,#f2dcc0);border-radius:6px}
.hero-art{left:370px;top:56px;width:276px;height:150px}
.wave{left:0;width:686px}
h2{font-size:13px;font-weight:700;color:var(--ink)}
p.copy{font-size:7.5px;line-height:1.65}
.link{font-size:8px;color:var(--orange);font-weight:500}
/* about */
.about-h{left:40px;top:300px}
.about-p{left:370px;top:294px;width:276px}
.about-link{left:370px;top:362px}
/* applications */
.apps-h{left:40px;top:410px}
.apps-p{left:40px;top:434px;width:270px}
.app-item{width:84px;text-align:center;font-size:8px;color:var(--teal);font-weight:500}
.app-ring{width:56px;height:56px;border:1.5px solid var(--teal);border-radius:50%;margin:0 auto 8px;display:flex;align-items:center;justify-content:center}
/* promise */
.promise-art{left:40px;top:504px;width:270px;height:132px}
.promise-h{left:370px;top:556px}
.promise-p{left:370px;top:580px;width:276px}
/* fragile */
.fragile-h{left:40px;top:738px}
.fragile-p{left:40px;top:762px;width:276px}
.fragile-art{left:380px;top:708px;width:266px;height:148px}
/* technology */
.tech-art{left:40px;top:930px;width:260px;height:118px}
.tech-h{left:370px;top:960px}
.tech-p{left:370px;top:984px;width:276px}
/* footer */
.site-footer{left:0;top:1068px;width:686px;height:132px;border-top:1px solid var(--line)}
.f-col{top:20px;font-size:7.5px;line-height:1.9}
.f-col h3{font-size:8.5px;font-weight:600;color:var(--orange);margin-bottom:4px}
.social{display:flex;gap:8px;margin-top:4px}
.social span{width:10px;height:10px;border-radius:50%;background:var(--ink)}
.copyright{left:40px;top:112px;font-size:6.5px;color:var(--muted)}
</style>
</head>
<body>

<header class="site-header abs">
  <div class="brand abs"><span class="brand-dot"></span>Antigen Preservation Bureau</div>
  <nav class="nav abs">
    <a class="active" href="#">Home</a><a href="#">About</a><a href="#">Services</a><a href="#">Applications</a><a href="#">Contact us</a>
  </nav>
</header>

<section class="hero">
  <h1 class="hero-title abs">We aim to provide services to stabilize various viruses, viral vectors and vaccines</h1>
  <p class="hero-text abs">APB has developed a proprietary formulation technology using blended amino acids. The technology is applied to an enveloped virus and stabilizes the virus in liquid and freeze-dried states.</p>
  <span class="btn abs">Discover more</span>
  <div class="hero-art art abs" role="img" aria-label="Illustration of a scientist with a microscope and laboratory flasks"></div>
  <svg class="wave abs" style="top:206px" width="686" height="50" viewBox="0 0 686 50" aria-hidden="true">
    <path d="M0 34 C180 6 420 4 686 24 L686 32 C420 14 200 18 0 44Z" fill="var(--gold)"/>
    <path d="M0 42 C200 20 430 20 686 32" stroke="var(--gold)" stroke-width="1" fill="none" opacity=".6"/>
  </svg>
</section>

<section class="about">
  <h2 class="about-h abs">About APB</h2>
  <p class="copy about-p abs">Vaccines are well-known effective tools for controlling infectious diseases. Recently, the first therapeutic virus has been approved and more are being evaluated in the clinic. In addition, recent progress has been made with gene-modified cell and gene therapies which require viral vectors to introduce exogenous genes.</p>
  <span class="link about-link abs">Contact us &rarr;</span>
</section>

<section class="applications">
  <h2 class="apps-h abs">Main Applications</h2>
  <p class="copy apps-p abs">Vaccines, therapeutic viruses, and viral vectors share the highly ordered complex structures and characteristics of viruses. Even at refrigerated temperatures.</p>
  <div class="app-item abs" style="left:392px;top:400px"><div class="app-ring"><svg width="22" height="22" viewBox="0 0 22 22" fill="none" stroke="var(--teal)" stroke-width="1.5"><rect x="3" y="8" width="16" height="7" rx="3.5"/><path d="M11 8v7"/></svg></div>Pharmaceutical</div>
  <div class="app-item abs" style="left:476px;top:400px"><div class="app-ring"><svg width="22" height="22" viewBox="0 0 22 22" fill="none" stroke="var(--teal)" stroke-width="1.5"><path d="M4 18l4-4M7 11l4 4M9 9l8-8M10 8l4 4-6 6-4-4z"/></svg></div>Vaccination</div>
  <div class="app-item abs" style="left:560px;top:400px"><div class="app-ring"><svg width="22" height="22" viewBox="0 0 22 22" fill="none" stroke="var(--teal)" stroke-width="1.5"><path d="M11 19s-7-4-7-9a4 4 0 017-2 4 4 0 017 2c0 5-7 9-7 9z"/></svg></div>Therapeutic</div>
</section>

<section class="promise">
  <div class="promise-art art abs" role="img" aria-label="Illustration of researchers working together in a laboratory"></div>
  <h2 class="promise-h abs">The Promise of Therapeutic Vaccines</h2>
  <p class="copy promise-p abs">Vaccines are well-known effective tools for controlling infectious diseases. Recently, the first therapeutic virus has been approved and more are being evaluated in the clinic. In addition, recent progress has been made with gene-modified cell and gene therapies which require viral vectors to introduce exogenous genes.</p>
  <svg class="wave abs" style="top:652px" width="686" height="46" viewBox="0 0 686 46" aria-hidden="true">
    <path d="M0 6 C200 36 420 36 686 14 L686 20 C420 42 200 42 0 14Z" fill="var(--gold)"/>
  </svg>
</section>

<section class="fragile">
  <h2 class="fragile-h abs">Viral Structures are Fragile</h2>
  <p class="copy fragile-p abs">Vaccines, therapeutic viruses, and viral vectors share the highly ordered complex structures and characteristics of viruses. Even at refrigerated temperatures, it is challenging to maintain their biological activity and other required characteristics of such biomolecules. Commercially available products require either refrigeration or frozen storage and transport. This cold chain requirement limits distribution and patient access.</p>
  <div class="fragile-art art abs" role="img" aria-label="Illustration of a scientist holding a test tube beside a flask"></div>
  <svg class="wave abs" style="top:862px" width="686" height="60" viewBox="0 0 686 60" aria-hidden="true">
    <path d="M0 34 C200 4 460 4 686 24 L686 32 C460 14 200 16 0 44Z" fill="var(--gold)"/>
    <path d="M0 50 C220 22 460 24 686 40" stroke="var(--gold)" stroke-width="1.2" fill="none"/>
  </svg>
</section>

<section class="technology">
  <div class="tech-art art abs" role="img" aria-label="Illustration of a research team holding vaccine vials and a clipboard"></div>
  <h2 class="tech-h abs">The Technology</h2>
  <p class="copy tech-p abs">Antigen Preservation Bureau (APB) has developed a proprietary formulation technology using blended amino acids. The technology is applied to an enveloped virus and stabilizes the virus in liquid and freeze-dried states.</p>
</section>

<footer class="site-footer abs">
  <div class="brand abs" style="left:40px;top:22px"><span class="brand-dot"></span>Antigen Preservation Bureau</div>
  <div class="f-col abs" style="left:300px"><h3>Company</h3>About<br>Applications<br>Career<br>Funding</div>
  <div class="f-col abs" style="left:420px"><h3>Address</h3>212 Meridian Lane<br>Harborview, CA, USA<br>(555) 010-2468<br>hello@apb-mail.org</div>
  <div class="f-col abs" style="left:560px"><h3>Find us on</h3><div class="social"><span></span><span></span><span></span><span></span></div></div>
  <p class="copyright abs">Copyright &copy; 2019. All right reserved</p>
</footer>

</body>
</html>
```